Fassadengestaltung für Werbetechniker
Zielgruppe
Wir sind eine Werbetechniker Firma die Lichtreklame, Fahrzeugbeschriftung , Schaufensterbeschriftung, Folierungen und Schilder anbietet. Unsere Zielgruppe sind Handwerker und Mittelständische Unternehmen.
Gestaltet werden soll unsere Fassade. Herausforderung sind die nicht symmetrisch angeordneten Fenster.
Aufgabenstellung
Einbindung unseres Firmennamens, was wir anbieten: Beschriftungen, Lichtwerbung , Schilder , Folierungen
Die Fassade soll auffällig sein eventuell schwarzer Hintergrund, ist aber nicht Voraussetzung.
Da wir das Design auf eine Fassadenfolie drucken wollen, könnten es auch andere Grafische Hintergründe sein.
Beispiele habe ich angehängt. Wie gesagt, wir lassen uns inspirieren.

```html
<!DOCTYPE html>
<html lang="de">
<head>
<meta charset="utf-8">
<title>Haftwerk Fassade</title>
<link rel="stylesheet" href="https://fonts.googleapis.com/css2?family=Archivo:ital,wght@0,500;0,800;1,500&family=Barlow+Condensed:wght@700&display=swap">
<style>
  :root {
    --backdrop: #d9d9d9;
    --panel: #2b2b2b;
    --white: #ffffff;
    --orange: #f07d00;
    --pink: #e0245e;
    --blue: #2a8fd0;
    --navy: #14183a;
    --yellow: #f4b51f;
  }
  * { margin: 0; padding: 0; box-sizing: border-box; }
  html, body { width: 906px; height: 1200px; overflow: hidden; background: var(--backdrop); }
  .facade {
    position: absolute; left: 31px; top: 412px;
    width: 845px; height: 375px; overflow: hidden;
  }
  .brand-panel {
    position: absolute; left: 0; top: 0; width: 105px; height: 100%;
    background: var(--panel);
  }
  .brand-name {
    position: absolute; left: 44px; top: 188px;
    transform: translate(-50%, -50%) rotate(-90deg);
    font-family: "Archivo", sans-serif; font-weight: 800;
    font-size: 58px; letter-spacing: -1px; line-height: 1;
    color: var(--white); white-space: nowrap;
  }
  .brand-tagline {
    position: absolute; left: 84px; top: 222px;
    transform: translate(-50%, -50%) rotate(-90deg);
    font-family: "Archivo", sans-serif; font-weight: 500;
    font-size: 15px; letter-spacing: 9px;
    color: var(--white); white-space: nowrap;
  }
  .artwork {
    position: absolute; left: 105px; top: 0; width: 740px; height: 100%;
    background:
      radial-gradient(ellipse at 55% 45%, var(--blue) 0%, rgba(42,143,208,0) 45%),
      radial-gradient(ellipse at 70% 30%, var(--pink) 0%, rgba(224,36,94,0) 40%),
      radial-gradient(circle at 10% 20%, var(--yellow) 0%, rgba(244,181,31,0) 25%),
      linear-gradient(120deg, var(--pink) 0%, var(--navy) 40%, var(--blue) 65%, var(--pink) 100%);
  }
  .window { position: absolute; background: var(--backdrop); }
  .services {
    position: absolute; left: 132px; top: 169px; width: 699px;
    transform: translateY(-50%);
    font-family: "Barlow Condensed", sans-serif; font-weight: 700;
    font-size: 27px; line-height: 1; color: var(--white);
    text-align: center; white-space: nowrap;
  }
  .slogan {
    position: absolute; left: 680px; top: 290px;
    transform: rotate(-32deg); transform-origin: left top;
    font-family: "Archivo", sans-serif; font-weight: 500; font-style: italic;
    color: var(--white); line-height: 1.05; white-space: nowrap;
  }
  .slogan .line-small { font-size: 17px; display: block; }
  .slogan .line-large { font-size: 21px; display: block; }
  .slogan .accent { color: var(--orange); }
</style>
</head>
<body>
  <section class="facade">
    <div class="brand-panel">
      <div class="brand-name">HAFTWERK</div>
      <div class="brand-tagline">WERBETECHNIK</div>
    </div>
    <div class="artwork" role="img" aria-label="Bunte Pop-Art-Illustration im Raster- und Punktstil in Pink, Blau, Gelb und Orange"></div>

    <div class="window" style="left:182px; top:36px; width:144px; height:92px;"></div>
    <div class="window" style="left:599px; top:36px; width:91px; height:94px;"></div>
    <div class="window" style="left:717px; top:36px; width:93px; height:93px;"></div>
    <div class="window" style="left:182px; top:207px; width:145px; height:95px;"></div>
    <div class="window" style="left:528px; top:210px; width:46px; height:60px;"></div>
    <div class="window" style="left:641px; top:211px; width:46px; height:58px;"></div>

    <div class="services">BESCHRIFTUNGEN | FOLIERUNGEN | LICHTWERBUNG | SCHILDER</div>

    <div class="slogan">
      <span class="line-small">MÖGE DAS</span>
      <span class="line-small"><span class="accent">HAFTWERK</span></span>
      <span class="line-large">MIT DIR SEIN.</span>
    </div>
  </section>
</body>
</html>
```